Business Card Design Project

Need business card for new non profit organization that includes the attached logo in some form.
with this information
Name: Martin Holloway Pryce
Title: President & Founder
A: P.O. Box 51637, Portland, Oregon, 97209-1637
E: marty@hollowayfoundation.org
E: marty@martypryce.com
P: 1.971.555.0172

```html
<!DOCTYPE html>
<html lang="en">
<head>
<meta charset="utf-8">
<title>Holloway Foundation – Business Card</title>
<link href="https://fonts.googleapis.com/css2?family=Montserrat:wght@600&family=Questrial&display=swap" rel="stylesheet">
<style>
  :root {
    --stage-grey: #d7d7d7;
    --card-white: #ffffff;
    --navy: #263170;
    --navy-deep: #1a2150;
    --navy-soft: #2b3a7c;
    --ink-light: #ffffff;
    --circle-navy: #2a3577;
  }
  html, body {
    margin: 0;
    padding: 0;
    width: 1200px;
    height: 1000px;
    overflow: hidden;
    background: var(--stage-grey);
  }
  .stage {
    position: relative;
    width: 1200px;
    height: 1000px;
  }
  .business-card {
    position: absolute;
    left: 211px;
    top: 273px;
    width: 777px;
    height: 454px;
    background: var(--card-white);
    overflow: hidden;
    font-family: "Questrial", "Century Gothic", sans-serif;
    color: var(--ink-light);
  }
  .diagonal-panel {
    position: absolute;
    inset: 0;
    clip-path: polygon(534px 0, 777px 0, 777px 454px, 0 454px);
    background:
      radial-gradient(ellipse 320px 260px at 640px 120px, rgba(60,76,150,0.35), transparent 70%),
      linear-gradient(135deg, var(--navy-soft) 0%, var(--navy) 45%, var(--navy-deep) 100%);
  }
  .brand-lockup {
    position: absolute;
    left: 52px;
    top: 82px;
    display: flex;
    align-items: center;
    gap: 14px;
  }
  .brand-dot {
    width: 58px;
    height: 58px;
    border-radius: 50%;
    background: var(--circle-navy);
  }
  .brand-name {
    font-family: "Questrial", "Century Gothic", sans-serif;
    font-size: 27px;
    line-height: 1.15;
    color: var(--navy);
  }
  .contact-block {
    position: absolute;
    left: 388px;
    top: 160px;
  }
  .person-name {
    font-family: "Montserrat", "Century Gothic", sans-serif;
    font-weight: 600;
    font-size: 21px;
    margin: 0;
    letter-spacing: 0.1px;
  }
  .person-title {
    font-size: 22px;
    margin: 7px 0 0;
  }
  .postal-address {
    font-style: normal;
    font-size: 19px;
    line-height: 25px;
    margin-top: 58px;
  }
  .contact-lines {
    list-style: none;
    margin: 13px 0 0;
    padding: 0;
    font-size: 19px;
    line-height: 26px;
  }
</style>
</head>
<body>
<main class="stage">
  <section class="business-card" aria-label="Business card for Martin Holloway Pryce">
    <div class="diagonal-panel"></div>

    <div class="brand-lockup">
      <span class="brand-dot"></span>
      <span class="brand-name">Holloway<br>Foundation</span>
    </div>

    <div class="contact-block">
      <h1 class="person-name">Martin Holloway Pryce</h1>
      <p class="person-title">President &amp; Founder</p>
      <address class="postal-address">P.O. Box 51637, Portland,<br>Oregon, 97209-1637</address>
      <ul class="contact-lines">
        <li>E: marty@hollowayfoundation.org</li>
        <li>E: marty@martypryce.com</li>
        <li>P: 1.971.555.0172</li>
      </ul>
    </div>
  </section>
</main>
</body>
</html>
```